Design a compelling Tarnwell Business Card that will drive people to my site

I want a business card that I can give to people—less to tell them who I am and more to direct them to my website. My website is a portal for Crestlane Aquatics Officials and a place for people who want to become Crestlane Aquatics Officials.
I am uploading my official company logo as well as a business card mockup that I did on my own. Please feel free to completely stray from this design.
I've included a screen recording of the homepage of my website as well.
Target Market(s)
Crestlane Aquatics Officials and people who desire to become one
Contact Information for Business Card
website url
Look and feel
Each slider illustrates characteristics of the customer's brand and the style your logo design should communicate.

```html
<!DOCTYPE html>
<html lang="en">
<head>
<meta charset="utf-8">
<title>Tarnwell Business Card</title>
<link rel="stylesheet" href="https://fonts.googleapis.com/css2?family=Poppins:wght@400;500;700&display=swap">
<style>
  :root {
    --backdrop: #1d1d20;
    --brand-blue: #3a52a4;
    --brand-deep: #2c4197;
    --brand-light: #8fa6dc;
    --card-white: #ffffff;
    --text-grey: #4a4a4f;
  }
  * { margin: 0; padding: 0; box-sizing: border-box; }
  html, body { width: 1200px; height: 900px; overflow: hidden; }
  body {
    background: var(--backdrop);
    font-family: "Poppins", sans-serif;
    position: relative;
  }
  .card {
    position: absolute;
    left: 250px;
    width: 700px;
    height: 400px;
    border-radius: 4px;
    overflow: hidden;
  }
  .card--front { top: 40px; background: var(--card-white); }
  .card--back { top: 460px; background: var(--brand-blue); }

  .contact-block { position: absolute; left: 56px; top: 96px; }
  .person-name {
    font-weight: 700;
    font-size: 26px;
    line-height: 1.1;
    color: var(--brand-deep);
  }
  .person-name .surname { color: var(--brand-light); }
  .person-role {
    font-size: 17px;
    color: var(--text-grey);
    margin-top: 4px;
  }
  .divider {
    position: absolute;
    left: 56px;
    top: 178px;
    width: 590px;
    height: 1px;
    background: var(--brand-light);
  }
  .divider::before {
    content: "";
    position: absolute;
    left: 0; top: -1px;
    width: 200px; height: 3px;
    background: var(--brand-deep);
  }
  .contact-list {
    position: absolute;
    left: 56px;
    top: 196px;
    list-style: none;
  }
  .contact-list li {
    display: flex;
    align-items: center;
    gap: 8px;
    font-size: 16px;
    line-height: 28px;
    color: var(--text-grey);
  }
  .contact-list svg { width: 14px; height: 14px; fill: var(--brand-deep); }

  .wordmark {
    position: absolute;
    font-weight: 700;
    letter-spacing: -1px;
    line-height: 1;
  }
  .card--front .wordmark {
    right: 54px;
    top: 96px;
    font-size: 66px;
    color: var(--brand-deep);
  }
  .card--back .wordmark {
    left: 0; right: 0;
    top: 120px;
    text-align: center;
    font-size: 96px;
    color: var(--card-white);
  }
  .tagline {
    position: absolute;
    left: 0; right: 0;
    top: 238px;
    text-align: center;
    font-size: 24px;
    color: var(--card-white);
  }
</style>
</head>
<body>
  <section class="card card--front">
    <div class="contact-block">
      <p class="person-name">Daniel <span class="surname">Morrow</span></p>
      <p class="person-role">CEO &amp; Founder</p>
    </div>
    <div class="divider"></div>
    <ul class="contact-list">
      <li>
        <svg viewBox="0 0 16 16" aria-hidden="true"><path d="M3 1h3l1.5 4-2 1.3a9 9 0 0 0 4.2 4.2L11 8.5l4 1.5v3a2 2 0 0 1-2 2A12 12 0 0 1 1 3a2 2 0 0 1 2-2z"/></svg>
        (555) 014-2273
      </li>
      <li>
        <svg viewBox="0 0 16 16" aria-hidden="true"><path d="M1 3h14v10H1zM2 4.2v.6l6 4 6-4v-.6z"/></svg>
        dan@tarnwell.com
      </li>
      <li>
        <svg viewBox="0 0 16 16" aria-hidden="true"><circle cx="8" cy="8" r="7"/><path d="M1 8h14M8 1c-3 4-3 10 0 14M8 1c3 4 3 10 0 14" stroke="#fff" stroke-width="1" fill="none"/></svg>
        www.tarnwell.com
      </li>
    </ul>
    <p class="wordmark">Tarnwell</p>
  </section>

  <section class="card card--back">
    <p class="wordmark">Tarnwell</p>
    <p class="tagline">Your Poolside Officials' Gateway</p>
  </section>
</body>
</html>
```